Brocure for Brindlo - Social Media Management

Brindlo is a Dutch company in the market of Social Media growth. We need a brochure (digital/PDF) for our company. Please see attached word doc for the text and attached logo. The initial proposal can contain just the first 4 pages text of the word doc.

We use informal language in all our communication.

Slogan: Effectieve Social Media Marketing voor professionals en ondernemers

Website: brindlopq.nl

Industry/Entity Type

Digital Marketing

Contact Information for Business Card

Contact details:

Joris ter Haaksel
joris@brindlopq.nl
06-47915328

```html
<!DOCTYPE html>
<html lang="nl">
<head>
<meta charset="utf-8">
<title>Brindlo – Brochure Social Media Marketing</title>
<link href="https://fonts.googleapis.com/css2?family=Poppins:wght@400;500;600;700;800&family=Oswald:wght@500&display=swap" rel="stylesheet">
<style>
  :root{
    --orange:#ec6a24;
    --navy:#27324a;
    --ink:#3a3a3a;
    --muted:#707070;
    --white:#ffffff;
    --stage-light:#ebe8e4;
  }
  html,body{margin:0;padding:0;width:1200px;height:2182px;overflow:hidden}
  body{position:relative;font-family:"Poppins",sans-serif;background:var(--stage-light)}
  .stage-top{position:absolute;left:0;top:0;width:1200px;height:940px;background:linear-gradient(180deg,#f1eeea,#e2ddd6)}
  .stage-bottom{position:absolute;left:0;top:940px;width:1200px;height:1242px;background:linear-gradient(180deg,#8d8d8d 0%,#4a4a4a 45%,#2b2b2b 100%)}

  .page{position:absolute;width:398px;height:515px;overflow:hidden;background:var(--white);box-shadow:0 6px 18px rgba(0,0,0,.25)}
  .cover-large{left:281px;top:58px;transform:scale(1.6);transform-origin:0 0;box-shadow:0 4px 12px rgba(0,0,0,.18)}

  /* brand */
  .brand{position:absolute;display:flex;align-items:center;gap:6px}
  .brand-dot{width:22px;height:22px;border-radius:50%;background:var(--orange)}
  .brand-name{font-weight:700;font-size:24px;letter-spacing:1px;color:var(--orange);line-height:1}

  /* cover */
  .cover .brand{right:36px;top:40px}
  .cover-photo{position:absolute;left:206px;top:117px;width:192px;height:283px;background:linear-gradient(135deg,#4a4037 0%,#2f3440 45%,#1d2533 100%)}
  .cover-visual{position:absolute;left:0;top:117px;width:206px;height:283px;background:linear-gradient(160deg,#ec6a24 0%,#9a4a3a 22%,#33395a 50%,#2a3550 100%)}
  .cover-title{position:absolute;left:38px;top:193px;color:var(--white)}
  .cover-kicker{display:inline-block;background:var(--orange);font-weight:600;font-size:15px;letter-spacing:1.6px;padding:1px 6px;line-height:18px}
  .cover-main{font-weight:800;font-size:20px;line-height:21px;margin-top:4px}
  .cover-sub{font-weight:400;font-size:16px;line-height:19px}
  .cover-rule{position:absolute;left:0;top:487px;width:228px;height:1px;background:var(--orange)}
  .cover-url{position:absolute;left:240px;top:479px;font-size:9px;letter-spacing:2px;color:var(--ink)}
  .cover-url b{color:var(--orange);font-weight:700}

  /* inner pages */
  .h{position:absolute;left:34px;margin:0;font-size:14.5px;font-weight:600;color:var(--orange);border-left:2px solid var(--orange);padding-left:11px;line-height:16px}
  .txt{position:absolute;left:34px;width:330px;margin:0;font-size:4.4px;line-height:6.3px;color:var(--muted)}
  .txt span{display:block;margin-bottom:2.5px}
  .bottom-rule{position:absolute;left:0;bottom:0;width:398px;height:2px;background:var(--orange)}

  .intro-band{position:absolute;left:0;top:0;width:398px;height:134px;background:var(--orange)}
  .intro-title{position:absolute;left:35px;top:22px;margin:0;padding-left:11px;border-left:2px solid var(--white);color:var(--white);font-size:15px;font-weight:600;line-height:19px}
  .intro-sub{position:absolute;left:47px;top:70px;color:var(--white);font-size:8.5px;font-weight:500;margin:0}
  .intro-txt{position:absolute;left:34px;top:86px;width:330px;font-size:4.4px;line-height:6.3px;color:#fde4d6;margin:0}
  .formula{position:absolute;left:34px;top:124px;width:330px;height:21px;background:var(--navy);color:var(--white);font-family:"Oswald",sans-serif;font-size:8.2px;line-height:21px;text-align:center}
  .visual-soft{position:absolute;border-radius:50%;background:radial-gradient(circle,#fde6da 0%,#eef3fa 60%,rgba(255,255,255,0) 72%)}
  .platform-lead{position:absolute;left:47px;top:428px;font-size:8px;font-weight:500;color:var(--ink);margin:0}
  .platforms{position:absolute;top:442px;display:grid;gap:5px}
  .platform{display:flex;align-items:flex-start;gap:5px;font-size:5.4px;line-height:6.4px;color:var(--ink)}
  .platform i{flex:none;width:11px;height:11px;border-radius:50%;background:var(--navy)}
  .platform.sm i{width:7px;height:7px;background:var(--orange)}
  .platform b{color:var(--orange);font-weight:600;display:block}

  .growth-band{position:absolute;left:0;top:268px;width:398px;height:152px;background:var(--orange)}
  .growth-text{position:absolute;left:0;top:0;width:211px;height:152px;background:var(--navy);box-sizing:border-box;padding:14px 12px 0 34px;color:#d7dbe4;font-size:4.4px;line-height:6.2px}
  .growth-text span{display:block;margin-bottom:4px}
  .growth-visual{position:absolute;left:211px;top:0;width:151px;height:152px;background:linear-gradient(135deg,#3f6ad8 0%,#5b8af0 55%,#8fb1f7 100%)}

  .top-line{position:absolute;left:34px;top:0;width:364px;height:2px;background:var(--navy)}
  .steps-band{position:absolute;left:0;top:231px;width:398px;height:207px;background:var(--orange)}
  .steps-band .edge{position:absolute;left:0;top:0;width:34px;height:207px;background:var(--navy)}
  .step{position:absolute;color:var(--white)}
  .step h3{margin:0 0 3px;font-size:6.6px;font-weight:500;display:flex;align-items:center;gap:3px}
  .step p{margin:0;font-size:4.1px;line-height:5.9px;color:#fde4d6}
  .contact-tab{position:absolute;left:34px;top:445px;width:330px;height:14px;border-bottom:1px solid var(--navy)}
  .contact-tab span{display:inline-block;background:var(--navy);color:var(--white);font-size:7.2px;font-weight:600;line-height:14px;padding:0 26px 0 14px;clip-path:polygon(0 0,88% 0,100% 100%,0 100%)}
  .contact{position:absolute;font-size:6.6px;line-height:10px;color:var(--ink)}
  .contact div{display:flex;align-items:center;gap:4px;height:10px}
  .contact-page .brand{left:220px;top:474px}
  .contact-page .brand-dot{width:16px;height:16px}
  .contact-page .brand-name{font-size:18px}
</style>
</head>
<body>
<div class="stage-top"></div>
<div class="stage-bottom"></div>

<!-- Cover (large) -->
<section class="page cover cover-large">
  <div class="brand"><span class="brand-dot"></span><span class="brand-name">BRINDLO</span></div>
  <div class="cover-visual" role="img" aria-label="Beeldmotief: vizier met social media pictogrammen"></div>
  <div class="cover-photo" role="img" aria-label="Foto: lachende ondernemer met tablet en laptop met social media dashboard"></div>
  <div class="cover-title">
    <span class="cover-kicker">EFFECTIEVE</span>
    <div class="cover-main">SOCIAL<br>MEDIA<br>MARKETING</div>
    <div class="cover-sub">voor professionals<br>en ondernemers</div>
  </div>
  <div class="cover-rule"></div>
  <div class="cover-url">www.<b>brindlopq</b>.nl</div>
</section>

<!-- Page 1: cover -->
<section class="page cover" style="left:168px;top:1014px">
  <div class="brand"><span class="brand-dot"></span><span class="brand-name">BRINDLO</span></div>
  <div class="cover-visual" role="img" aria-label="Beeldmotief: vizier met social media pictogrammen"></div>
  <div class="cover-photo" role="img" aria-label="Foto: lachende ondernemer met tablet en laptop met social media dashboard"></div>
  <div class="cover-title">
    <span class="cover-kicker">EFFECTIEVE</span>
    <div class="cover-main">SOCIAL<br>MEDIA<br>MARKETING</div>
    <div class="cover-sub">voor professionals<br>en ondernemers</div>
  </div>
  <div class="cover-rule"></div>
  <div class="cover-url">www.<b>brindlopq</b>.nl</div>
</section>

<!-- Page 2: introduction -->
<section class="page" style="left:646px;top:1014px">
  <div class="intro-band"></div>
  <h1 class="intro-title">Social Media Marketing voor<br>zakelijke professionals en ondernemers</h1>
  <p class="intro-sub">Groei, interactie en content</p>
  <p class="intro-txt">Je bereik vergroten, traffic genereren en daarmee meer omzet behalen. Dat is wat wij bieden.<br>Onze services helpen jouw bereik op de sociale media te vergroten. Met een uitgekiende groeistrategie, onze kennis en geavanceerde tools zorgen we voor gerichte content en interactie op je sociale netwerken.</p>
  <div class="formula">((actieve interactie + relevante content) &gt; actieve volgers) = (&gt; traffic + omzet)</div>

  <h2 class="h" style="top:162px">Wie zijn wij?</h2>
  <p class="txt" style="top:183px;width:172px"><span>Wij zijn Brindlo. Een team van sociale media experts dat je sociale netwerk activeert en het bereik vergroot. We zorgen voor sociale interactie met volgers, nieuwe en bestaande. Daarmee genereren we traffic naar je website of shop.</span><span>Het doel? Meer omzet. Simpel en heel meetbaar.</span></p>
  <div class="visual-soft" role="img" aria-label="Illustratie: hand met smartphone omringd door social media meldingen" style="left:228px;top:150px;width:150px;height:150px"></div>

  <h2 class="h" style="top:236px">Voor wie?</h2>
  <p class="txt" style="top:256px;width:172px">Onze dienstverlening kan ingezet worden op zowel persoonlijke zakelijke profielen, of voor bedrijfspagina's op diverse sociale mediakanalen.</p>

  <h2 class="h" style="top:290px">Wat doen we?</h2>
  <p class="txt" style="top:311px"><span>Samen met jou bepalen we je doelen in de sociale netwerken. Zowel strategisch als tactisch en operationeel. Wij richten ons op die doelen en zorgen voor een netwerk van echte en actieve volgers.</span><span>Of het nu gaat om Netprofiel, Beeldstroom, Kringplein of Kortbericht, interactie zorgt voor betrokken volgers. Die zijn vervolgens in je verkoopproces kunt oppakken.</span><span>Voor zakelijke professionals verzorgen wij personal branding met als doel impact en social sales. We zorgen voor veel meer relevante connecties en activeren je zakelijke netwerk. Gecombineerd met de juiste contentstrategie, zorgen wij ervoor dat je gezien wordt als autoriteit in je vakgebied.</span><span>Onze diensten voor bedrijven bestaan uit de versnelde organische groei van het volgernetwerk, het activeren van het netwerk met content en interactie. We zorgen daarmee voor een groot bereik en verkeer naar je website.</span></p>

  <h2 class="h" style="top:408px">Welke platformen?</h2>
  <p class="platform-lead">We bieden onze diensten aan op alle belangrijke platformen:</p>
  <div class="platforms" style="left:36px">
    <div class="platform"><i></i><div><b>Netprofiel</b>(bedrijfspagina's en persoonlijke profielen)</div></div>
    <div class="platform"><i></i><div><b>Kringplein</b>(bedrijfspagina's en groepen)</div></div>
    <div class="platform"><i></i><div><b>Beeldstroom</b>(bedrijfspagina's en persoonlijke profielen)</div></div>
  </div>
  <div class="platforms" style="left:228px;gap:4px;top:446px">
    <div class="platform sm"><i></i><div><b>Kortbericht</b></div></div>
    <div class="platform sm"><i></i><div><b>Kijkkanaal</b></div></div>
    <div class="platform sm"><i></i><div><b>Zoekkaart Zakelijk</b></div></div>
    <div class="platform sm"><i></i><div><b style="color:var(--ink)">Optioneel:</b>Klipto, Prikwand, Draadforum en Blogvel</div></div>
  </div>
  <div class="bottom-rule"></div>
</section>

<!-- Page 3: why us -->
<section class="page" style="left:168px;top:1583px">
  <h2 class="h" style="top:26px">Waarom kies je voor ons?</h2>
  <p class="txt" style="top:46px"><span>Jij hebt jouw vak, wij het onze. Als iedereen doet waar hij goed in is, worden daar allemaal beter van. Wij zijn goed in het activeren en vergroten van je sociale netwerk. Daarvoor gebruiken we een slimme mix van kennis en tools.</span><span>Een strategie die ervoor zorgt dat jij je kunt focussen op je corebusiness. Met onze slimme tools vergroten wij de impact van je sociale netwerken. Met als resultaat: meer traffic, meer leads, meer omzet.</span></p>

  <h2 class="h" style="top:96px">Doen we alles zelf?</h2>
  <p class="txt" style="top:116px"><span>Wij zijn slim in de strategie en systemen voor het vergroten van interactie. En we hebben een netwerk van specialisten die slim zijn in hun vak. Zoals een reclamebureau, creatief ontwerper, websitebouwer of marketingstrategiebureau.</span><span>Is er op dat vlak een behoefte, dan brengen wij je graag in contact.</span></p>

  <h2 class="h" style="top:166px">Hoe lang gaan we met elkaar in zee?</h2>
  <p class="txt" style="top:186px"><span>Een groeistrategie werkt op de lange termijn het beste als de groei organisch is. En dat vraagt dus ook een strategie voor de lange termijn. Lang is relatief, maar je moet erop rekenen dat we minimaal een jaar nodig hebben om de groeistrategie optimaal te laten werken.</span><span>Natuurlijk is er in elke situatie snelle winst te behalen. Maar voor een goede samenwerking is het belangrijk dat je elkaar leert kennen en begrijpen. Daarom vragen we ook regelmatig jouw energie en input.</span></p>

  <h2 class="h" style="top:248px">Groeien op sociale media</h2>
  <div class="growth-band">
    <div class="growth-text"><span>Het staat als een paal boven water: sociale media zijn een krachtig marketinginstrument. Een kans die je niet voorbij kunt laten gaan, of je dat nou leuk vindt of niet. Het geeft je de kans om je merk op te bouwen, je zicht- en vindbaarheid te verbeteren en uiteindelijk meer leads en verkopen te genereren.</span><span>Het beheren van je sociale platforms is een tijdrovende klus. En om resultaat te krijgen, moet je het ook nog eens slim doen. Om de online herkenbaarheid van je bedrijf te vergroten, zijn je uitingen de sleutel.</span><span>Interactie, consistentie, responsiveness, allemaal zorgen ze voor herkenning en betrokkenheid van je volgers. We helpen je om je digitale activiteiten met elkaar te verbinden en je bedrijf te laten groeien.</span></div>
    <div class="growth-visual" role="img" aria-label="Illustratie: magneet die volgers en meldingen aantrekt"></div>
  </div>

  <h2 class="h" style="top:458px">Volledig sociaal management</h2>
  <p class="txt" style="top:478px"><span>We bieden een compleet beheerpakket voor sociale media waarmee we betrokkenheid van volgers realiseren en tijdig en altijd proactief schakelen naar de volgende stap. Zo blijven bezoekers geboeid en actief.</span><span>We plannen zowel doelgroep- als branche specifieke inhoud en combineren online aanwezigheid om meer en meer gericht websiteverkeer te genereren.</span></p>
  <div class="bottom-rule"></div>
</section>

<!-- Page 4: network, approach, contact -->
<section class="page contact-page" style="left:646px;top:1583px">
  <div class="top-line"></div>
  <h2 class="h" style="top:26px">Activeren van je netwerk</h2>
  <p class="txt" style="top:46px"><span>Je bent al een poos bezig met het beheren van je sociale media, maar ziet geen commercieel resultaat? De specialist maakt het verschil. Jouw kennis van jouw product en klant, gecombineerd met ons specialisme over sociale media. In zeer diverse branches.</span><span>Wij gebruiken deze kennis voor een contentstrategie op maat. Een strategie die gegarandeerd meer likes, retweets en doorkliks genereert. Meer likes, meer interactie, meer betrokkenheid, meer omzet.</span></p>

  <h2 class="h" style="top:109px">Groeistrategie</h2>
  <p class="txt" style="top:129px"><span>Je netwerk op sociale media laten groeien kan een lastige klus zijn. Maar het levert je enorm veel op. Een groot aantal echte en actieve volgers geeft vertrouwen en genereert nog meer betrokkenheid. Het is de moderne variant van mond-tot-mondreclame.</span><span>Wij hebben de expertise en oplossingen om al je profielen een echte boost te geven. Met onze tools krijgen we de volledige controle over je kanalen, zodat jij jouw focus kunt richten op de uitvoering en levering van opdrachten.</span><span>En wees voorbereid op groei!</span></p>

  <h2 class="h" style="top:209px">Hoe werkt het?</h2>
  <div class="steps-band">
    <div class="edge"></div>
    <div class="step" style="left:50px;top:11px;width:164px">
      <h3><svg width="6" height="6" viewBox="0 0 6 6"><circle cx="3" cy="3" r="2.6" fill="none" stroke="#fff" stroke-width=".6"/><path d="M1.8 3.1l.8.8 1.6-1.7" fill="none" stroke="#fff" stroke-width=".6"/></svg>Quick Scan &amp; advies</h3>
      <p>We starten altijd met een grondige analyse van je website en sociale kanalen. Op basis daarvan geven we je een advies over de beste strategie.</p>
    </div>
    <div class="step" style="left:50px;top:58px;width:164px">
      <h3><svg width="6" height="6" viewBox="0 0 6 6"><circle cx="3" cy="3" r="2.6" fill="none" stroke="#fff" stroke-width=".6"/><path d="M1.8 3.1l.8.8 1.6-1.7" fill="none" stroke="#fff" stroke-width=".6"/></svg>Pakketkeuze</h3>
      <p>We hebben verschillende servicepakketten waaruit je kunt kiezen wat bij jouw situatie en wensen past. Blijkt op basis van de Quick Scan dat je beter af bent met maatwerk, dan maken we daarover specifieke afspraken.</p>
      <p style="margin-top:3px">Geen twee klanten zijn gelijk, daarom is ons aanbod flexibel opgebouwd.</p>
    </div>
    <div class="step" style="left:50px;top:136px;width:164px">
      <h3><svg width="6" height="6" viewBox="0 0 6 6"><circle cx="3" cy="3" r="2.6" fill="none" stroke="#fff" stroke-width=".6"/><path d="M1.8 3.1l.8.8 1.6-1.7" fill="none" stroke="#fff" stroke-width=".6"/></svg>Terugkoppeling en verbetering</h3>
      <p>Iedere ondernemer is gedreven als het gaat om het behalen van resultaten. Zo ook wij. Wij doen er alles aan om onze dienstverlening zo succesvol mogelijk te laten zijn en jouw sociale doelen te behalen. We hebben regelmatig contact om de resultaten te bespreken en daar waar mogelijk te verbeteren.</p>
    </div>
    <div class="step" style="left:226px;top:11px;width:160px">
      <h3><svg width="6" height="6" viewBox="0 0 6 6"><circle cx="3" cy="3" r="2.6" fill="none" stroke="#fff" stroke-width=".6"/><path d="M1.8 3.1l.8.8 1.6-1.7" fill="none" stroke="#fff" stroke-width=".6"/></svg>Je wilt met ons in zee</h3>
      <p>Als je besluit met ons in zee te gaan, doen we dat niet voor een paar weken. Want we doen niet aan hit- and-run, maar bouwen aan samenwerking die op de lange termijn echte resultaten oplevert. We moeten elkaar goed leren kennen en dat vraagt tijd.</p>
      <p style="margin-top:3px">Je vertrouwt ons je sociale mediakanalen toe. Dat vraagt vertrouwen en tegelijk moeten wij ons goed inleven in de manier van communicatie die past bij jouw business en jouw doelgroep. Van beide kanten vraagt dit een tijdsinvestering.</p>
    </div>
    <div class="step" style="left:226px;top:108px;width:160px">
      <h3><svg width="6" height="6" viewBox="0 0 6 6"><circle cx="3" cy="3" r="2.6" fill="none" stroke="#fff" stroke-width=".6"/><path d="M1.8 3.1l.8.8 1.6-1.7" fill="none" stroke="#fff" stroke-width=".6"/></svg>Implementatie</h3>
      <p>Natuurlijk wil je zo snel mogelijk resultaat zien. Dat willen wij ook. We werken de strategie uit in een plan en gaan voor jou aan het werk. Met de prioriteit op die gebieden die zo snel mogelijk resultaten opleveren. Omdat we graag (laten) zien wat onze inspanningen verschil maken.</p>
      <p style="margin-top:3px">We richten daarvoor de benodigde systemen in. In het begin hebben we regelmatig overleg om elkaar goed te leren kennen en de vinger aan de pols te houden.</p>
    </div>
  </div>

  <div class="contact-tab"><span>NEEM DAN CONTACT OP</span></div>
  <div class="contact" style="left:38px;top:472px">
    <div><svg width="6" height="7" viewBox="0 0 6 7"><path d="M3 .4a2.2 2.2 0 0 1 2.2 2.2C5.2 4.2 3 6.6 3 6.6S.8 4.2.8 2.6A2.2 2.2 0 0 1 3 .4z" fill="#ec6a24"/><circle cx="3" cy="2.6" r=".8" fill="#fff"/></svg>Kanaalweg 27, 6716XR Ede</div>
    <div><svg width="7" height="5" viewBox="0 0 7 5"><rect x=".3" y=".3" width="6.4" height="4.4" fill="none" stroke="#ec6a24" stroke-width=".6"/><path d="M.3.3l3.2 2.4L6.7.3" fill="none" stroke="#ec6a24" stroke-width=".6"/></svg>info@brindlopq.nl&nbsp;&nbsp;<svg width="6" height="6" viewBox="0 0 6 6"><circle cx="3" cy="3" r="2.6" fill="none" stroke="#ec6a24" stroke-width=".6"/><path d="M2 1.7l.6.9-.4.4c.3.6.6.9 1.2 1.2l.4-.4.9.6-.5.6C2.9 4.8 1.2 3.1 1.4 2.2z" fill="#ec6a24"/></svg>06-47915328</div>
    <div><svg width="6" height="6" viewBox="0 0 6 6"><circle cx="3" cy="3" r="2.6" fill="none" stroke="#ec6a24" stroke-width=".6"/><ellipse cx="3" cy="3" rx="1.1" ry="2.6" fill="none" stroke="#ec6a24" stroke-width=".5"/><line x1=".4" y1="3" x2="5.6" y2="3" stroke="#ec6a24" stroke-width=".5"/></svg>www.brindlopq.nl</div>
  </div>
  <div class="brand"><span class="brand-dot"></span><span class="brand-name">BRINDLO</span></div>
  <div class="bottom-rule"></div>
</section>
</body>
</html>
```